Fresh Nest Builder Guide needs a new Landing Page

I like to get a landing page or website with 2-3 pages to help target home buyers who are looking to buy homes from builders such as PV Dwellings, Moritz, G.T. Falwick, etc. The landing page/website to be non-cluttered and be able to explain to home buyers that there are many benefits to include me as their buyer's agent when they buy a brand new home from any builders.
I may want to incorporate a short explanation video (animated) on the landing page and then for the viewer to click on a button that will take them to another page where they can search for new homes from different builders.
Target Market(s)
Home buyers looking to buy brand new home from builders such as PV Dwellings, Moritz, G.T. Falwick, etc.
Industry/Entity Type
Real Estate
Number of Pages Required
2 page
Requirements
Must have
- The landing page may have the explanation video at the bottom of the landing page (scrolled down) or there may be a CALL TO ACTION button that takes the viewer to the 2nd page to watch the explanation video. Once they watched the explanation video and are still interested, they can click on another CALL TO ACTION button that will take them to another website that they will be able to search for all the available new homes and register their contact information.
Should not have
- No clutters and no dark colors.

```html
<!DOCTYPE html>
<html lang="en">
<head>
<meta charset="utf-8">
<title>Fresh Nest Builder Guide — Find Your Comfort Zone</title>
<link rel="stylesheet" href="https://fonts.googleapis.com/css2?family=Arimo:wght@400;700&family=Roboto:wght@300;400&family=Lato:wght@400;700&display=swap">
<style>
  :root {
    --ink: #333333;
    --ink-soft: #555555;
    --green: #5aab80;
    --green-band: #5cad80;
    --orange: #f6812c;
    --white: #ffffff;
    --footer: #3e3e3e;
    --footer-text: #d8d8d8;
  }
  * { box-sizing: border-box; margin: 0; padding: 0; }
  html, body { width: 1200px; height: 2899px; overflow: hidden; }
  body {
    position: relative;
    background: var(--white);
    font-family: "Arimo", Arial, sans-serif;
    color: var(--ink);
  }
  .abs { position: absolute; }

  /* Navigation */
  .site-nav { position: absolute; top: 0; left: 0; width: 1200px; height: 106px; background: var(--white); }
  .site-nav a {
    position: absolute; top: 55px; font-size: 13px; letter-spacing: 0.6px;
    color: #777; text-decoration: none; text-transform: uppercase;
  }
  .site-nav a.is-current { color: var(--ink); }

  /* Hero */
  .hero {
    position: absolute; top: 106px; left: 0; width: 1200px; height: 657px;
    background: linear-gradient(180deg, #b9bec4 0%, #8a7a6a 14%, #6b4a33 28%, #4d3b30 40%, #8a8a82 52%, #5d8793 62%, #3f6a78 78%, #2f5260 100%);
  }
  .hero-search {
    position: absolute; top: 541px; left: 421px; width: 259px; height: 54px;
    background: var(--orange); color: var(--white);
    font-family: "Lato", Arial, sans-serif; font-weight: 700; font-size: 36px;
    letter-spacing: 1px; text-align: center; line-height: 54px;
  }

  /* Intro */
  .intro-title {
    top: 808px; left: 0; width: 1200px; text-align: center;
    font-family: "Roboto", Arial, sans-serif; font-weight: 300;
    font-size: 43px; letter-spacing: 2px; color: var(--ink);
  }
  .eyebrow {
    font-size: 12.5px; letter-spacing: 1.4px; color: var(--green); text-transform: uppercase;
  }
  .intro-eyebrow { top: 933px; left: 0; width: 1200px; text-align: center; }

  .promo-video {
    top: 991px; left: 301px; width: 597px; height: 334px;
    background: linear-gradient(180deg, #5a3a2c 0%, #8a5034 35%, #3f5f72 62%, #2c2f36 100%);
    overflow: hidden;
  }
  .promo-caption {
    position: absolute; left: 0; width: 100%; text-align: center;
    font-family: "Lato", Arial, sans-serif; color: var(--white);
  }
  .promo-question { top: 225px; font-size: 24px; }
  .promo-price { top: 256px; font-size: 40px; font-weight: 700; }
  .player-bar { position: absolute; left: 0; bottom: 0; width: 100%; height: 32px; background: rgba(0,0,0,0.55); }
  .player-track { position: absolute; left: 12px; right: 12px; top: 4px; height: 3px; background: rgba(255,255,255,0.35); }
  .player-progress { width: 4%; height: 100%; background: #e62117; }
  .player-time { position: absolute; left: 108px; top: 12px; font-size: 10px; color: var(--white); }

  .btn-pill {
    display: block; text-align: center; text-transform: uppercase;
    border-radius: 24px; text-decoration: none;
  }
  .search-properties {
    top: 1385px; left: 518px; width: 207px; height: 45px; line-height: 45px;
    background: var(--green); color: var(--white); font-size: 12.5px; letter-spacing: 0.6px;
  }

  /* Feature sections */
  .photo { position: absolute; }
  .photo-modern-home {
    top: 1518px; left: 158px; width: 460px; height: 356px;
    background: linear-gradient(180deg, #3f4a66 0%, #8a93a8 35%, #d7d6d8 55%, #7a8490 75%, #3c4a55 100%);
  }
  .photo-for-sale {
    top: 1982px; left: 647px; width: 389px; height: 298px;
    background: linear-gradient(180deg, #cfd6d6 0%, #e8e6e0 30%, #b7b3a8 55%, #8a9a50 78%, #c8b050 100%);
  }
  .section-title {
    font-family: "Roboto", Arial, sans-serif; font-weight: 300;
    font-size: 43px; line-height: 44px; letter-spacing: 1.5px; color: var(--ink);
  }
  .body-copy { font-size: 12px; line-height: 17.5px; color: var(--ink-soft); }

  .love-title { top: 1540px; left: 703px; width: 380px; }
  .love-eyebrow { top: 1643px; left: 703px; }
  .love-copy-1 { top: 1688px; left: 703px; width: 352px; }
  .love-copy-2 { top: 1783px; left: 703px; width: 352px; }

  .talk-title { top: 1984px; left: 238px; }
  .talk-eyebrow { top: 2069px; left: 238px; font-weight: 700; font-size: 12px; }
  .talk-copy { top: 2086px; left: 238px; width: 352px; }
  .benefit-list { top: 2170px; left: 234px; list-style: none; }
  .benefit-list li {
    position: relative; height: 30.5px; padding-left: 30px;
    font-size: 12px; line-height: 18px; color: var(--ink-soft);
  }
  .benefit-list svg { position: absolute; left: 0; top: 1px; }

  /* Subscribe */
  .subscribe { position: absolute; top: 2390px; left: 0; width: 1200px; height: 377px; background: var(--green-band); }
  .subscribe-title {
    position: absolute; top: 105px; width: 100%; text-align: center;
    font-family: "Roboto", Arial, sans-serif; font-weight: 300;
    font-size: 42px; letter-spacing: 2px; color: var(--white);
  }
  .subscribe-sub {
    position: absolute; top: 160px; width: 100%; text-align: center;
    font-size: 12px; letter-spacing: 1.4px; color: #dff0e6;
  }
  .field {
    position: absolute; top: 224px; height: 45px; border: 2px solid var(--white);
    border-radius: 24px; color: var(--white); font-size: 13px; letter-spacing: 0.5px;
    line-height: 41px; padding-left: 16px; text-transform: uppercase;
  }
  .field-name { left: 311px; width: 209px; }
  .field-email { left: 529px; width: 209px; }
  .subscribe-submit {
    position: absolute; top: 224px; left: 753px; width: 136px; height: 45px; line-height: 45px;
    background: var(--white); color: var(--green); font-size: 13px; letter-spacing: 0.8px;
  }

  /* Footer */
  .site-footer { position: absolute; top: 2767px; left: 0; width: 1200px; height: 132px; background: var(--footer); }
  .footer-brand {
    position: absolute; top: 56px; left: 150px; width: 100px;
    font-size: 12px; font-weight: 700; line-height: 14px; color: var(--white);
  }
  .footer-copyright { position: absolute; top: 58px; left: 267px; font-size: 12.5px; font-weight: 700; color: var(--white); }
  .footer-links { position: absolute; top: 84px; left: 267px; font-size: 11.5px; color: var(--footer-text); }
  .footer-links span { margin: 0 14px; }
  .social { position: absolute; top: 52px; width: 37px; height: 37px; border-radius: 50%; }
  .social-one { left: 918px; background: var(--green); }
  .social-two { left: 962px; background: #2e2e2e; }
  .social-three { left: 1006px; background: #2e2e2e; }
</style>
</head>
<body>

<nav class="site-nav">
  <a class="is-current" style="left:357px">Home</a>
  <a style="left:427px">About Us</a>
  <a style="left:528px">Services</a>
  <a style="left:611px">Foreclosure</a>
  <a style="left:734px">Portfolio</a>
</nav>

<header class="hero" role="img" aria-label="Photo of a lodge-style wooden house lit at dusk, reflected in a pool">
  <div class="hero-search">SEARCH</div>
</header>

<h1 class="abs intro-title">FIND YOUR COMFORT ZONE</h1>
<p class="abs eyebrow intro-eyebrow">Watch our promotional video</p>

<div class="abs promo-video" role="img" aria-label="Promotional video frame showing a house with a lit pool at night">
  <p class="promo-caption promo-question">HOW MUCH TO CHARGE FOR REAL ESTATE?</p>
  <p class="promo-caption promo-price">$1,500 - $2,500</p>
  <div class="player-bar">
    <div class="player-track"><div class="player-progress"></div></div>
    <svg class="abs" style="left:12px;top:12px" width="90" height="14" viewBox="0 0 90 14" fill="#fff">
      <polygon points="2,2 11,7 2,12"/>
      <polygon points="30,3 36,7 30,11"/><rect x="37" y="3" width="2" height="8"/>
      <polygon points="58,5 62,5 66,2 66,12 62,9 58,9"/>
      <path d="M69 4 Q72 7 69 10" stroke="#fff" stroke-width="1.4" fill="none"/>
    </svg>
    <span class="player-time">0:24 / 19:58</span>
    <svg class="abs" style="right:12px;top:11px" width="100" height="12" viewBox="0 0 100 12" fill="none" stroke="#fff" stroke-width="1.4">
      <rect x="2" y="2" width="12" height="8"/>
      <circle cx="34" cy="6" r="4"/>
      <rect x="56" y="2" width="14" height="8"/>
      <path d="M86 1h-4v4M94 1h4v4M86 11h-4v-4M94 11h4v-4"/>
    </svg>
  </div>
</div>

<a class="abs btn-pill search-properties">Search Properties</a>

<div class="photo photo-modern-home" role="img" aria-label="Photo of a modern white house with large windows beside a reflecting pool at dusk"></div>
<h2 class="abs section-title love-title">WE LOVE REAL ESTATE</h2>
<p class="abs eyebrow love-eyebrow">See your ideal home brought to life</p>
<p class="abs body-copy love-copy-1">Lorem ipsum dolor sit amet, consectetur adipiscing elit. Duis gravida blandit lacus a laoreet. Nullam sollicitudin urna metus, at malesuada orci fringilla in. Curabitur eleifend risus vitae ligula semper scelerisque. Nulla sed nisl nulla.</p>
<p class="abs body-copy love-copy-2">Fusce interdum suscipit ipsum, quis mattis metus posuere sit amet. Mauris rutrum imperdiet tortor.</p>

<h2 class="abs section-title talk-title">LET’S TALK</h2>
<p class="abs eyebrow talk-eyebrow">We’re here to listen to your needs</p>
<p class="abs body-copy talk-copy">Lorem ipsum dolor sit amet, consectetur adipiscing elit. Duis gravida blandit lacus a laoreet. Nullam sollicitudin urna metus, at malesuada orci fringilla in.</p>
<ul class="abs benefit-list">
  <li><svg width="18" height="18" viewBox="0 0 18 18"><circle cx="9" cy="9" r="9" fill="var(--green)"/><path d="M5 9.2l2.6 2.6L13 6.4" stroke="#fff" stroke-width="2" fill="none"/></svg>Curabitur eleifend risus vitae ligula semper scelerisque.</li>
  <li><svg width="18" height="18" viewBox="0 0 18 18"><circle cx="9" cy="9" r="9" fill="var(--green)"/><path d="M5 9.2l2.6 2.6L13 6.4" stroke="#fff" stroke-width="2" fill="none"/></svg>Fusce interdum suscipit ipsum.</li>
  <li><svg width="18" height="18" viewBox="0 0 18 18"><circle cx="9" cy="9" r="9" fill="var(--green)"/><path d="M5 9.2l2.6 2.6L13 6.4" stroke="#fff" stroke-width="2" fill="none"/></svg>Quis mattis metus posuere sit amet.</li>
  <li><svg width="18" height="18" viewBox="0 0 18 18"><circle cx="9" cy="9" r="9" fill="var(--green)"/><path d="M5 9.2l2.6 2.6L13 6.4" stroke="#fff" stroke-width="2" fill="none"/></svg>Mauris rutrum imperdiet tortor.</li>
</ul>
<div class="photo photo-for-sale" role="img" aria-label="Photo of a for-sale sign in front of a white two-storey house"></div>

<section class="subscribe">
  <h2 class="subscribe-title">SUBSCRIBE</h2>
  <p class="subscribe-sub">STAY UP TO DATE WITH US</p>
  <div class="field field-name">Your Name</div>
  <div class="field field-email">Email Address</div>
  <a class="btn-pill subscribe-submit">Submit</a>
</section>

<footer class="site-footer">
  <div class="footer-brand">FRESH NEST</div>
  <p class="footer-copyright">COPYRIGHT 2016 © REAL ESTATE</p>
  <p class="footer-links">Contact Us<span>|</span>Terms &amp; Conditions<span>|</span>Privacy</p>
  <a class="social social-one" aria-label="Social link"></a>
  <a class="social social-two" aria-label="Social link"></a>
  <a class="social social-three" aria-label="Social link"></a>
</footer>

</body>
</html>
```